Lakemont Hydro Partners, Inc. Company Brochure

I would like someone to design a brochure that can be handed out to prospective clients. We are a full service water and wastewater operations company that provides services to Municipal Utility Districts and citys. I would like something that is catchy to the eye and reflects a company that prides itself on providing personal service to its clients. We need to revamp our website, that's next, but the website does have a description of our company and services offered. You can find that information at www.lakemonthydropartners.example

```html
<!DOCTYPE html>
<html lang="en">
<head>
<meta charset="utf-8">
<title>Lakemont Hydro Partners, Inc. – Brochure</title>
<link href="https://fonts.googleapis.com/css2?family=PT+Sans:wght@400;700&family=Ubuntu:wght@500&display=swap" rel="stylesheet">
<style>
  :root{
    --blue:#1a7fd4;
    --blue-deep:#0b4f9c;
    --blue-ink:#163a6b;
    --sky:#cfe6fb;
    --sky-pale:#eaf5fe;
    --text:#2a3a55;
    --paper:#ffffff;
    --stage:#eef1f4;
  }
  *{box-sizing:border-box;margin:0;padding:0}
  html,body{width:1185px;height:1200px;overflow:hidden}
  body{background:var(--stage);font-family:"PT Sans",sans-serif;color:var(--text)}
  .spread{position:absolute;left:212px;width:760px;height:570px;background:var(--paper);box-shadow:0 2px 10px rgba(0,0,0,.18);overflow:hidden}
  .spread--outside{top:20px}
  .spread--inside{top:610px}
  .spread__art{position:absolute;inset:0}
  .fold{position:absolute;left:380px;top:0;width:1px;height:100%;background:rgba(0,0,0,.06)}
  .heading{position:absolute;font-family:"Ubuntu",sans-serif;font-weight:500;font-size:25px;color:var(--blue);display:flex;align-items:center;gap:10px}
  .heading__dot{width:18px;height:18px;border:2.5px solid var(--blue);border-radius:50%}
  .copy{position:absolute;font-size:10.2px;line-height:1.25}
  .copy p+p{margin-top:11px}
  .contact{position:absolute;left:28px;top:475px;font-size:14px;color:var(--blue-ink);line-height:1.2}
  .contact strong{font-size:15px;margin-left:6px}
  .contact .address{margin-top:4px;font-size:13.5px}
  .web{position:absolute;font-weight:700;font-size:12px;color:var(--blue-ink)}
  .brand{position:absolute;left:380px;top:30px;width:380px;text-align:center}
  .brand__dot{width:30px;height:30px;border:3px solid var(--blue);border-radius:50%;margin:0 auto 14px}
  .brand__name{font-weight:700;font-size:24px;color:var(--blue)}
  .brand__tag{font-size:15px;color:var(--blue-ink);margin-top:6px}
  .photo{position:absolute}
  .services-list{position:absolute;left:420px;top:182px;width:320px;list-style:none;font-size:11.2px;font-weight:700;color:var(--blue-ink);line-height:1.1}
  .services-list li{position:relative;padding-left:16px;margin-bottom:5.2px}
  .services-list li::before{content:"";position:absolute;left:0;top:4px;width:6px;height:6px;border-radius:50%;background:var(--blue)}
  .slogan{position:absolute;right:18px;top:510px;text-align:right;color:#fff;font-weight:700;font-size:17px;line-height:1.1}
</style>
</head>
<body>

<!-- Outside spread: mission panel and front cover -->
<section class="spread spread--outside">
  <svg class="spread__art" viewBox="0 0 760 570" width="760" height="570">
    <defs>
      <linearGradient id="paleWave" x1="0" y1="0" x2="0" y2="1">
        <stop offset="0" stop-color="#bcdcf8"/><stop offset="1" stop-color="#f2f9ff"/>
      </linearGradient>
      <linearGradient id="dropletTone" x1="0" y1="0" x2="1" y2="1">
        <stop offset="0" stop-color="#0d4fa8"/><stop offset=".5" stop-color="#2f86dc"/><stop offset="1" stop-color="#1563c0"/>
      </linearGradient>
    </defs>
    <path d="M0,195 C220,205 420,225 760,150 L760,535 C560,545 300,520 0,540 Z" fill="url(#paleWave)"/>
    <path d="M0,195 C220,205 420,225 760,150" fill="none" stroke="var(--blue)" stroke-width="4"/>
    <path d="M0,215 C220,228 440,240 760,175" fill="none" stroke="#fff" stroke-width="6" opacity=".8"/>
    <g role="img" aria-label="Close-up photograph of water droplets on a blue surface">
      <path d="M0,300 C180,290 380,310 760,235 L760,420 C520,420 300,450 0,455 Z" fill="url(#dropletTone)"/>
    </g>
    <path d="M0,455 C300,450 520,420 760,420 L760,445 C520,445 300,480 0,480 Z" fill="#fff" opacity=".55"/>
    <path d="M0,520 C260,500 520,480 760,510 L760,570 L0,570 Z" fill="#fff"/>
    <path d="M380,570 C520,530 660,520 760,530" fill="none" stroke="var(--blue)" stroke-width="3"/>
  </svg>
  <div class="fold"></div>

  <h2 class="heading" style="left:22px;top:16px"><span class="heading__dot"></span>Our Mission</h2>
  <div class="copy" style="left:22px;top:58px;width:335px">
    <p>Lakemont Hydro Partners, Inc. is a leading competitor in the utility operations industry and has achieved this status by maintaining the quality of work and relationships that few companies can offer.</p>
    <p>Whether you are a District that is currently operated by an outside contract company or a District entertaining the concept, Lakemont Hydro Partners, Inc would be delighted to present a detailed quote for operations and services. Please contact our office and a representative will discuss the services that are currently available in your area.</p>
  </div>
  <div class="contact">
    <div>Office: <strong>555-201-4870</strong></div>
    <div>Toll Free <strong style="margin-left:0">800-555-0147</strong></div>
    <div class="address">4820 Lakeview Rd #210<br>Marlow, TX 75510</div>
  </div>

  <div class="brand">
    <div class="brand__dot"></div>
    <div class="brand__name">Lakemont Hydro Partners, Inc.</div>
    <div class="brand__tag">A Full Service Operations Company</div>
  </div>
  <div class="web" style="left:460px;top:543px">www.lakemonthydropartners.example</div>
</section>

<!-- Inside spread: about us and services -->
<section class="spread spread--inside">
  <svg class="spread__art" viewBox="0 0 760 570" width="760" height="570">
    <defs>
      <linearGradient id="plantTone" x1="0" y1="0" x2="0" y2="1">
        <stop offset="0" stop-color="#c9dde8"/><stop offset=".45" stop-color="#7ea9bf"/><stop offset="1" stop-color="#9fc4d6"/>
      </linearGradient>
      <linearGradient id="glassTone" x1="0" y1="0" x2="1" y2="1">
        <stop offset="0" stop-color="#8cc0ec"/><stop offset=".6" stop-color="#2a7bd0"/><stop offset="1" stop-color="#0f5cb8"/>
      </linearGradient>
    </defs>
    <path d="M380,230 C520,210 640,240 760,225 L760,440 C620,430 500,460 380,445 Z" fill="#e8f3fd" opacity=".8"/>
    <path d="M0,405 C240,440 520,400 760,420" fill="none" stroke="#bcdcf8" stroke-width="10" opacity=".8"/>
    <path d="M0,420 C240,455 520,415 760,435" fill="none" stroke="#d9ecfc" stroke-width="6"/>
    <g role="img" aria-label="Photograph of a water treatment plant clarifier basin">
      <rect x="0" y="445" width="380" height="125" fill="url(#plantTone)"/>
    </g>
    <g role="img" aria-label="Photograph of water being poured into a glass against blue sky">
      <path d="M380,460 C520,450 640,465 760,455 L760,570 L380,570 Z" fill="url(#glassTone)"/>
    </g>
  </svg>
  <div class="fold"></div>

  <h2 class="heading" style="left:28px;top:18px"><span class="heading__dot"></span>About Us</h2>
  <div class="copy" style="left:28px;top:60px;width:205px">
    <p>Lakemont Hydro Partners, Inc. was incorporated in the state of Texas in 1989.</p>
    <p style="margin-top:4px">Lakemont Hydro Partners, Inc. is a water and waste water utility operations and billing company.</p>
    <p style="margin-top:4px">All personnel employed by Lakemont Hydro Partners, Inc. are licensed by the TWQB in water &amp; waste water operations and obtain the proper training needed to successfully operate treatment plants to their maximum capability.</p>
  </div>
  <div class="photo" role="img" aria-label="Photograph of a kitchen faucet filling a glass of water" style="left:240px;top:62px;width:125px;height:135px;background:linear-gradient(160deg,#8f9aa8,#d8dde3 60%,#b8c2cc)"></div>
  <div class="copy" style="left:28px;top:214px;width:320px">
    <p>We are certified to operate surface water, ground water, and waste water treatment facilities to their maximum capability.</p>
  </div>
  <div class="photo" role="img" aria-label="Photograph of a lab technician holding test tubes" style="left:15px;top:248px;width:160px;height:125px;background:linear-gradient(135deg,#c8d3e4,#8fa3c4 55%,#dfe6f0)"></div>
  <div class="copy" style="left:185px;top:250px;width:165px">
    <p>We have a fully staffed billing and collections office to handle any of your customers needs.</p>
    <p style="margin-top:4px">The mission of Lakemont Hydro Partners, Inc. is to provide the consumer with the highest caliber of services available.</p>
  </div>
  <div class="copy" style="left:28px;top:382px;width:320px">
    <p>Our goal is to achieve this service for the Districts with the most competitive cost around.</p>
  </div>

  <h2 class="heading" style="left:408px;top:18px"><span class="heading__dot"></span>Services</h2>
  <div class="copy" style="left:408px;top:60px;width:325px">
    <p>Lakemont Hydro Partners, Inc. is a "full service" operations company that handles all aspects of operations in the water/waste water utility industry.</p>
    <p>Here at Lakemont Hydro Partners, Inc, we feel that it is important to provide the highest caliber of services available to the Districts in which we operate. We offer the ability to tailor our services based on the current needs of the District.</p>
    <p style="font-weight:700;font-size:11px;color:var(--blue-ink);margin-top:6px">Services currently available are:</p>
  </div>
  <ul class="services-list">
    <li>Surface Water Plant Operations</li>
    <li>Waste Water Plant Operations</li>
    <li>Ground Water Well Operations</li>
    <li>Distribution and Collection System maintenance and repairs</li>
    <li>New Construction Water and Sewer Taps, and all inspections required</li>
    <li>Billing and Collections</li>
    <li>Meter Reading</li>
    <li>Consulting/Management</li>
    <li>Lab Work and Reporting to any and all regulating agencies</li>
    <li>Project Planning</li>
    <li>Assist in Annual Budget Planning</li>
    <li>Smoke Testing</li>
    <li>Park and Trail maintenance</li>
    <li>Detention pond maintenance</li>
  </ul>
  <div class="slogan">We are a 24/7<br>Operations Company!</div>
</section>

</body>
</html>
```